24 hour coin operated Pulse Harbor Workout Center Grand opening.

We are the first of our kind on the planet. I have invented and opened three 24 hour coin operated cardio centers. It's a gym with no weights and no classes. It only has cardio equipment. Imagine a laundromat or a video game arcade, only the machines are treadmills, cross trainers, stair steppers, bikes, etc. my sales person is a coin changer. I have no employees that work in the gym. It's fully automated. I am opening my fourth location and would like to announce its opening, while offering a special pre sale pricing for my tokens. The pre sale pricing is only good until about a week after I open and then the tokens will be regular price. The price is buy 40 tokens get 10 free. My opening day is expected to be Septmebr 14th, so bonus offer ends on the 22nd of Septemebr. I am hoping for a unique design to go along with our unique fitness style.

Target Market(s)

Men and Women from the ages of 14 to 65. all ages really.

Industry/Entity Type

Fitness

Font styles to use
Sans Serif

Colors
fbed22
000000

Requirements
Must have
• Our name and logo P Harbor Workout
• Our FB access name FB:PULSEHARBORWORKOUT
• Must say 24 hours
• Must say worlds first coin operated cardio center.
• Must say grand opening special offer ends Septemebr 22nd
• Phone number: 0958467291
• Must have our address and map:
• No.47, Minsheng Rd., Anping Dist., Tainan City 708 (see attached men for map)
Nice to have
• Website: pulseharborworkout-example.com
Should not have
• Please don't worry about the Chinese characters If I haven't asked you to add them. Sorry, this is to save time for those who haven't been selected.

```html
<!DOCTYPE html>
<html lang="en">
<head>
<meta charset="utf-8">
<title>P Harbor Workout – Grand Opening</title>
<link href="https://fonts.googleapis.com/css2?family=Questrial&family=Oswald:wght@600&display=swap" rel="stylesheet">
<style>
  :root {
    --yellow: #fbed22;
    --yellow-shade: #e2d21c;
    --black: #000000;
    --ink: #1a1a1a;
    --white: #ffffff;
    --star-grey: #e4e4e4;
    --photo-light: #d9dde0;
    --photo-mid: #9a9ea2;
    --photo-dark: #4a4b4d;
    --map-light: #d6d2ca;
    --map-dark: #c4c0b6;
    --map-border: #f4f1ea;
  }
  html, body {
    margin: 0;
    padding: 0;
    overflow: hidden;
    background: var(--white);
  }
  .poster {
    position: relative;
    width: 848px;
    height: 1200px;
    overflow: hidden;
    font-family: "Questrial", sans-serif;
    color: var(--ink);
    background: var(--yellow);
  }
  .hero-photo {
    position: absolute;
    inset: 0 0 auto 0;
    height: 640px;
    background: linear-gradient(160deg, var(--photo-light) 0%, var(--photo-mid) 45%, var(--photo-dark) 100%);
  }
  .shapes {
    position: absolute;
    inset: 0;
  }
  .brand-mark {
    position: absolute;
    left: 50px;
    top: 38px;
    width: 116px;
    height: 116px;
    border-radius: 50%;
    background: var(--black);
  }
  .brand-name {
    position: absolute;
    left: 0;
    top: 0;
    margin: 0;
    font-weight: 400;
    color: var(--ink);
    line-height: 1;
  }
  .brand-name span {
    position: absolute;
    white-space: nowrap;
  }
  .brand-initial { left: 226px; top: 56px; font-size: 48px; }
  .brand-main { left: 216px; top: 110px; font-size: 128px; letter-spacing: 2px; }
  .brand-sub { right: -792px; top: 246px; font-size: 62px; letter-spacing: -1px; }
  .open-badge {
    position: absolute;
    left: 586px;
    top: 420px;
    width: 220px;
    height: 200px;
  }
  .open-badge p {
    position: absolute;
    inset: 0;
    margin: 0;
    display: flex;
    flex-direction: column;
    justify-content: center;
    align-items: center;
    font-size: 36px;
    line-height: 0.92;
    text-align: center;
    letter-spacing: -1px;
  }
  .headline {
    position: absolute;
    left: 54px;
    top: 526px;
    margin: 0;
    font-weight: 400;
    line-height: 1;
    text-transform: uppercase;
  }
  .headline .small { display: block; font-size: 58px; letter-spacing: 2px; margin-bottom: 2px; }
  .headline .large { display: block; font-size: 86px; letter-spacing: 1px; margin-top: -4px; }
  .offer {
    position: absolute;
    left: 54px;
    top: 812px;
    margin: 0;
    font-size: 50px;
    line-height: 52px;
  }
  .map {
    position: absolute;
    left: 426px;
    top: 638px;
    width: 404px;
    height: 404px;
    border-radius: 50%;
    background: radial-gradient(circle at 40% 35%, var(--map-light) 0%, var(--map-dark) 100%);
    border: 6px solid var(--map-border);
    box-sizing: border-box;
  }
  .footer {
    position: absolute;
    left: 0;
    bottom: 0;
    width: 100%;
    height: 96px;
    background: var(--black);
    color: var(--white);
    font-family: "Oswald", sans-serif;
    font-weight: 600;
  }
  .footer-call {
    position: absolute;
    left: 62px;
    top: 10px;
    line-height: 1;
  }
  .footer-call .label { display: block; font-size: 19px; }
  .footer-call .phone { display: block; font-size: 40px; letter-spacing: 0.5px; margin-top: 2px; }
  .footer-info {
    position: absolute;
    left: 318px;
    top: 18px;
    margin: 0;
    font-size: 16px;
    line-height: 30px;
    white-space: nowrap;
    display: grid;
    grid-template-columns: auto auto;
    column-gap: 8px;
  }
  .footer-info dt, .footer-info dd { margin: 0; }
  .footer-info .fb-value { padding-left: 56px; }
</style>
</head>
<body>
<main class="poster">
  <div class="hero-photo" role="img" aria-label="Photo of a runner's legs and shoes on a treadmill in a bright gym"></div>

  <svg class="shapes" width="848" height="1200" viewBox="0 0 848 1200" aria-hidden="true">
    <polygon fill="var(--yellow)" points="0,384 76,296 160,352 264,320 344,376 440,368 440,544 530,520 640,480 848,624 848,1200 0,1200"/>
    <polygon fill="var(--yellow)" points="720,0 848,0 848,118 736,118"/>
    <polygon fill="var(--yellow)" points="640,56 716,48 676,100"/>
    <polygon fill="var(--yellow)" points="210,186 262,250 196,236"/>
    <polygon fill="var(--yellow)" points="250,234 330,266 300,226"/>
    <polygon fill="var(--yellow)" points="340,290 420,318 360,350"/>
    <polygon fill="var(--yellow)" points="712,148 768,186 720,210"/>
    <polygon fill="var(--yellow)" points="772,236 820,262 780,282"/>
    <polygon fill="var(--yellow-shade)" points="236,380 300,324 280,480"/>
    <polygon fill="var(--yellow-shade)" points="0,1120 108,1100 30,1190"/>
  </svg>

  <div class="brand-mark" aria-hidden="true"></div>
  <h1 class="brand-name" aria-label="P Harbor Workout">
    <span class="brand-initial">P</span>
    <span class="brand-main">HARBOR</span>
    <span class="brand-sub">WORKOUT</span>
  </h1>

  <div class="open-badge">
    <svg width="220" height="200" viewBox="0 0 220 200" aria-hidden="true">
      <polygon fill="var(--star-grey)" points="110,4 134,52 190,34 172,84 218,110 168,126 180,180 128,156 104,198 86,150 30,168 48,118 2,96 54,76 40,24 92,46"/>
    </svg>
    <p>OPEN<br>24<br>HOURS</p>
  </div>

  <h2 class="headline">
    <span class="small">First Coin</span>
    <span class="small">Operated</span>
    <span class="large">Cardio</span>
    <span class="large">Center</span>
  </h2>

  <p class="offer">Grand Opening<br>Special Offer<br>Ends<br>September 22nd</p>

  <div class="map" role="img" aria-label="Street map showing the center's location on Minsheng Rd., Anping Dist."></div>

  <footer class="footer">
    <div class="footer-call">
      <span class="label">CALL US</span>
      <span class="phone">0958467291</span>
    </div>
    <dl class="footer-info">
      <dt>ADDRESS:</dt>
      <dd>No.47, Minsheng Rd., Anping Dist., Tainan City 708</dd>
      <dt>FACEBOOK:</dt>
      <dd class="fb-value">pulseharborworkout-example.com/fb</dd>
    </dl>
  </footer>
</main>
</body>
</html>
```